Hair Extension Packaging

Update 2/16 - please keep submissions coming, I have no front runners yet. Thanks.

I need some new packaging designed for hair extensions. I have enclose pictures of what other companies packaging looks like and a few pictures of some inspiration. I am looking for a packaging that will appeal to a 20's-30's year old demographic and I like things along the lines of glamor/lace/vintage/boudoir/damask inspired. I am going to leave colors up to your creativity for the sample artwork and ask for changes if needed. Id like the design to be a standout but not loud.

The working name for this hair is "Velvetta"
Additional Text that I would like on the packaging "100% Premium Virgin Remy Human Hair"

Please keep in mind that the background of the packaging will have many different colors laying over it so be mindful of what the color you chose can effect the hair color in the packaging - no red or orange which can make the hair appear very warm and clash with ashy colors.

Working dimensions for the sample are 22" long, 3" wide.

****Once I decide on the front of the packaging I will also need the back designed which will consist of similar design as the front but with hair care instructions printed on it.***** This finished product must include front and back artwork, open Photoshop files, and additional bleed room for printing. I don't want to waste anyone's time so once I get a front design I like I will work with that artist to create the back.

Please message me with any questions.
Updates

Project Deadline Extended
Reason: Finalizing final choices. Thanks for your submissions!

Target Market(s)

Women in there 20"s - 30's. High fashion, luxurious, glamour

Industry/Entity Type

Hair

Font styles to use
Serif
Script

Requirements
Must have
• Id love the product name to be in script and then mixed with regular font (see the makeup logo example I enclosed)
Should not have
• Should not be masculine. Forget the blue and green colors

```html
<!DOCTYPE html>
<html lang="en">
<head>
<meta charset="utf-8">
<title>Velvetta Hair Extension Packaging</title>
<link rel="stylesheet" href="https://fonts.googleapis.com/css2?family=Poiret+One&family=Great+Vibes&family=Arimo:wght@400&display=swap">
<style>
  :root {
    --page: #ffffff;
    --hair-light: #c6a274;
    --hair-mid: #6e4c2f;
    --hair-dark: #2b1b10;
    --backdrop: #f3e6ad;
    --cream: #f7efc9;
    --rose: #96587a;
    --rose-soft: #d7a9c3;
    --champagne: #a8874f;
    --champagne-soft: #e8d7a8;
    --onyx: #111111;
    --onyx-soft: #6a6a6a;
    --plum: #7b2f78;
    --plum-soft: #bf78b9;
  }
  html, body {
    margin: 0;
    padding: 0;
    overflow: hidden;
    background: var(--page);
  }
  .canvas {
    position: relative;
    width: 1200px;
    height: 1200px;
    background: var(--page);
    overflow: hidden;
  }
  .pack {
    position: absolute;
    top: 36px;
    width: 156px;
    height: 1140px;
    display: flex;
    flex-direction: column;
    box-shadow: 0 0 0 1px rgba(0,0,0,0.1);
  }
  .pack--rose      { left: 160px; --accent: var(--rose);      --accent-soft: var(--rose-soft); }
  .pack--champagne { left: 370px; --accent: var(--champagne); --accent-soft: var(--champagne-soft); }
  .pack--onyx      { left: 584px; --accent: var(--onyx);      --accent-soft: var(--onyx-soft); }
  .pack--plum      { left: 856px; --accent: var(--plum);      --accent-soft: var(--plum-soft); }

  .pack__header {
    position: relative;
    height: 144px;
    flex: none;
    background: linear-gradient(180deg, var(--accent-soft) 0%, #f5f3f3 60%, #ffffff 100%);
    text-align: center;
    overflow: hidden;
  }
  .pack__frame {
    position: absolute;
    top: 5px;
    left: 5px;
    right: 5px;
    bottom: 22px;
    border: 1px solid var(--accent);
    outline: 1px solid var(--accent);
    outline-offset: -4px;
    opacity: 0.35;
    border-radius: 2px;
  }
  .pack__hanger {
    position: absolute;
    top: 4px;
    left: 50%;
    width: 22px;
    height: 11px;
    margin-left: -11px;
    background: #ffffff;
    border-radius: 6px 6px 2px 2px;
  }
  .pack__brand {
    margin: 26px 0 0;
    font-family: 'Poiret One', sans-serif;
    font-size: 32px;
    line-height: 1;
    color: var(--accent);
    font-weight: 400;
  }
  .pack--onyx .pack__brand { color: #6f6f6f; }
  .pack__brand--script {
    font-family: 'Great Vibes', cursive;
    font-size: 40px;
    margin-top: 20px;
  }
  .pack__tagline {
    margin: 10px 0 0;
    font-family: 'Arimo', sans-serif;
    font-size: 12px;
    line-height: 1.3;
    color: var(--accent);
  }
  .pack__curve {
    position: absolute;
    left: 0;
    bottom: 0;
    width: 156px;
    height: 26px;
  }
  .pack__hair {
    flex: 1;
    position: relative;
    background:
      linear-gradient(90deg,
        var(--backdrop) 0%, var(--hair-mid) 10%, var(--hair-light) 20%, var(--hair-dark) 30%,
        var(--hair-light) 41%, var(--hair-mid) 51%, var(--hair-light) 61%, var(--hair-dark) 71%,
        var(--hair-light) 81%, var(--hair-mid) 90%, var(--backdrop) 100%);
  }
  .pack__hair::after {
    content: "";
    position: absolute;
    inset: 0;
    background: linear-gradient(180deg, rgba(0,0,0,0.08) 0%, rgba(0,0,0,0) 40%, rgba(30,15,5,0.45) 100%);
  }
  .pack__band {
    position: relative;
    height: 122px;
    flex: none;
    background: var(--accent);
  }
  .pack__band::before {
    content: "";
    position: absolute;
    top: -6px;
    left: 0;
    right: 0;
    height: 6px;
    background: radial-gradient(circle at 6px 6px, var(--accent) 5px, transparent 5.5px) 0 0 / 12px 6px repeat-x;
  }
  .pack__band::after {
    content: "";
    position: absolute;
    inset: 8px;
    border: 1px solid rgba(255,255,255,0.35);
    outline: 1px solid rgba(255,255,255,0.2);
    outline-offset: -4px;
  }
</style>
</head>
<body>
<div class="canvas">

  <div class="pack pack--rose">
    <div class="pack__header">
      <span class="pack__frame"></span>
      <span class="pack__hanger"></span>
      <h2 class="pack__brand">Velvetta</h2>
      <p class="pack__tagline">100% Premium Virgin<br>Remy Human Hair</p>
      <svg class="pack__curve" viewBox="0 0 156 26" aria-hidden="true">
        <path d="M0 26 Q78 2 156 26 Z" fill="#f7efc9"/>
        <path d="M0 26 Q78 2 156 26" fill="none" stroke="#96587a" stroke-width="2.5"/>
      </svg>
    </div>
    <div class="pack__hair" role="img" aria-label="Long straight brown hair with blonde highlights"></div>
    <div class="pack__band"></div>
  </div>

  <div class="pack pack--champagne">
    <div class="pack__header">
      <span class="pack__frame"></span>
      <span class="pack__hanger"></span>
      <h2 class="pack__brand">Velvetta</h2>
      <p class="pack__tagline">100% Premium Virgin<br>Remy Human Hair</p>
      <svg class="pack__curve" viewBox="0 0 156 26" aria-hidden="true">
        <path d="M0 26 Q78 2 156 26 Z" fill="#f7efc9"/>
        <path d="M0 26 Q78 2 156 26" fill="none" stroke="#a8874f" stroke-width="2.5"/>
      </svg>
    </div>
    <div class="pack__hair" role="img" aria-label="Long straight brown hair with blonde highlights"></div>
    <div class="pack__band"></div>
  </div>

  <div class="pack pack--onyx">
    <div class="pack__header">
      <span class="pack__frame"></span>
      <span class="pack__hanger"></span>
      <h2 class="pack__brand">Velvetta</h2>
      <p class="pack__tagline">100% Premium Virgin<br>Remy Human Hair</p>
      <svg class="pack__curve" viewBox="0 0 156 26" aria-hidden="true">
        <path d="M0 26 Q78 2 156 26 Z" fill="#f7efc9"/>
        <path d="M0 26 Q78 2 156 26" fill="none" stroke="#9a9a9a" stroke-width="2.5"/>
      </svg>
    </div>
    <div class="pack__hair" role="img" aria-label="Long straight brown hair with blonde highlights"></div>
    <div class="pack__band"></div>
  </div>

  <div class="pack pack--plum">
    <div class="pack__header">
      <span class="pack__frame"></span>
      <span class="pack__hanger"></span>
      <h2 class="pack__brand pack__brand--script">Velvetta</h2>
      <p class="pack__tagline">100% Premium Virgin<br>Remy Human Hair</p>
      <svg class="pack__curve" viewBox="0 0 156 26" aria-hidden="true">
        <path d="M0 26 Q78 2 156 26 Z" fill="#f7efc9"/>
        <path d="M0 26 Q78 2 156 26" fill="none" stroke="#7b2f78" stroke-width="2.5"/>
      </svg>
    </div>
    <div class="pack__hair" role="img" aria-label="Long straight brown hair with blonde highlights"></div>
    <div class="pack__band"></div>
  </div>

</div>
</body>
</html>
```